Instructions for nurses on how to give a report on each shift

I have a 2-page reference sheet that needs to be updated to look more aesthetically pleasing.

Target Market(s)

Healthcare, nurses

Industry/Entity Type

Healthcare

Font styles to use
Sans Serif

Requirements
Must have
• Please make sure it is easy to read, the content is well organized and has a flow to it. Please also pick colors that would coordinate with our website www.ovtrime.org (so mainly navy and white or off-white with accent colors.) Please make sure to add accent colors to break up the content. The BORSK name and title at the top should remain on the page but I'm not married to the star or logo style. You can do what you think looks best there. Way at the bottom in fine print, I would like for you to add OVTRIME © 2019 All rights reserved.

```html
<!DOCTYPE html>
<html lang="en">
<head>
<meta charset="utf-8">
<title>BORSK – Shift Report Reference</title>
<link rel="stylesheet" href="https://fonts.googleapis.com/css2?family=Arimo:wght@400;700&family=Tinos&family=Courgette&display=swap">
<style>
  :root {
    --navy: #0f2a44;
    --ink: #2b2f7a;
    --grey: #58595b;
    --soft-grey: #6d6e71;
    --white: #ffffff;
    --text: #1d1d1d;
  }
  * { margin: 0; padding: 0; box-sizing: border-box; }
  html, body { width: 1200px; height: 898px; overflow: hidden; background: var(--white); }
  body { position: relative; font-family: "Arimo", Arial, sans-serif; color: var(--text); }

  .brand { position: absolute; left: 30px; top: 2px; }
  .brand-name { font-family: "Tinos", "Times New Roman", serif; font-size: 64px; line-height: 1; color: var(--navy); letter-spacing: 1px; }
  .brand-tagline { margin-top: 6px; font-size: 16.5px; line-height: 23px; color: var(--soft-grey); text-transform: uppercase; }

  .motto { position: absolute; left: 430px; width: 500px; top: 10px; text-align: center; font-family: "Courgette", cursive; color: var(--ink); font-size: 29px; line-height: 44px; }

  .section-title { position: absolute; top: 138px; font-size: 33px; font-weight: 700; color: var(--grey); letter-spacing: 0.5px; text-align: center; }
  .section-title.objectives { left: 132px; width: 509px; }
  .section-title.outcomes { left: 668px; width: 396px; }

  .card { position: absolute; background: var(--navy); border-radius: 14px; color: var(--white); font-size: 16px; }
  .card.objectives { left: 132px; top: 183px; width: 509px; height: 187px; padding-top: 33px; }
  .card.outcomes { left: 668px; top: 183px; width: 396px; height: 187px; padding-top: 39px; }
  .card.who { left: 52px; top: 389px; width: 521px; height: 194px; }
  .card.when { left: 598px; top: 389px; width: 323px; height: 194px; }
  .card.where { left: 947px; top: 389px; width: 205px; height: 194px; }

  .objective-list { display: grid; grid-template-columns: 171px 1fr; column-gap: 12px; row-gap: 4px; font-size: 16.5px; line-height: 18px; }
  .objective-list dt { text-align: right; font-weight: 700; }
  .objective-list dt::after { content: ":"; }

  .bullet-list { list-style: none; }
  .bullet-list li { position: relative; }
  .bullet-list li::before { content: "•"; position: absolute; }

  .outcome-list { padding-left: 111px; font-size: 16.5px; line-height: 26px; }
  .outcome-list li::before { left: -55px; }

  .vertical-label { position: absolute; top: 0; bottom: 0; width: 60px; display: flex; align-items: center; justify-content: center; }
  .vertical-label span { transform: rotate(-90deg); font-weight: 700; font-size: 47px; letter-spacing: 1px; white-space: nowrap; }
  .who .vertical-label { left: 10px; }
  .when .vertical-label { left: 12px; }
  .where .vertical-label { left: 12px; }

  .who-list { position: absolute; left: 83px; top: 16px; right: 10px; font-size: 16.5px; line-height: 25px; }
  .who-list li { padding-left: 14px; }
  .who-list li::before { left: 0; }
  .who-list li.wrap { line-height: 21px; margin-top: 3px; }

  .when-text { position: absolute; left: 87px; top: 32px; right: 12px; font-size: 16.5px; line-height: 21px; }
  .when-text p + p { margin-top: 19px; }
  .where-text { position: absolute; left: 70px; top: 34px; right: 8px; font-size: 16.5px; line-height: 21px; }

  .tips-band { position: absolute; left: 0; top: 600px; width: 1200px; height: 267px; background: var(--navy); color: var(--white); }
  .tips-list { position: absolute; left: 121px; top: 43px; font-size: 16.5px; line-height: 25.5px; }
  .tips-list li { padding-left: 13px; }
  .tips-list li::before { left: 0; }
  .tips-badge { position: absolute; left: 876px; top: 21px; width: 188px; height: 188px; }
  .tips-badge-text { position: absolute; left: 876px; top: 21px; width: 188px; height: 188px; display: flex; flex-direction: column; align-items: center; justify-content: center; color: var(--navy); font-weight: 700; font-size: 26px; line-height: 31px; letter-spacing: 0.5px; }

  .footer-note { position: absolute; left: 0; width: 1200px; top: 877px; text-align: center; font-size: 15px; color: #111; }
</style>
</head>
<body>
  <header class="brand">
    <div class="brand-name">BORSK</div>
    <div class="brand-tagline">Sharing clear, caring shift<br>reports for every nurse</div>
  </header>

  <div class="motto">When "I" is replaced by "WE"<br>Even illness becomes wellness.</div>

  <h2 class="section-title objectives">OBJECTIVES</h2>
  <h2 class="section-title outcomes">OUTCOMES</h2>

  <section class="card objectives">
    <dl class="objective-list">
      <dt>Accountability</dt><dd>Declare roles and assignments</dd>
      <dt>Advocacy</dt><dd>Identify patient needs</dd>
      <dt>Critical Thinking</dt><dd>Prioritize and recognize obstacles</dd>
      <dt>Communication</dt><dd>Share important information</dd>
      <dt>Collaboration</dt><dd>Utilize an interdisciplinary approach</dd>
    </dl>
  </section>

  <section class="card outcomes">
    <ul class="bullet-list outcome-list">
      <li>Share best practices</li>
      <li>Improve communication</li>
      <li>Promote cohesiveness</li>
      <li>Increase staff morale</li>
    </ul>
  </section>

  <section class="card who">
    <div class="vertical-label"><span>WHO</span></div>
    <ul class="bullet-list who-list">
      <li>All nurses on the unit</li>
      <li>All nursing support staff (CNA/MA/HCT)</li>
      <li>Administrator</li>
      <li>Director of Nursing</li>
      <li class="wrap">Head of pertinent disciplines (Dietary, Social Work, Physical Therapy, Engineering, Central Supply, etc.)</li>
    </ul>
  </section>

  <section class="card when">
    <div class="vertical-label"><span>WHEN</span></div>
    <div class="when-text">
      <p>Every morning (assign a meeting time for each unit)</p>
      <p>Keep meetings within 15 minutes in length</p>
    </div>
  </section>

  <section class="card where">
    <div class="vertical-label"><span>WHERE</span></div>
    <div class="where-text">Nursing station on each unit</div>
  </section>

  <section class="tips-band">
    <ul class="bullet-list tips-list">
      <li>Assign a meeting facilitator (usually the administrator of the facility)</li>
      <li>Standing during meetings keeps the meetings short and to the point</li>
      <li>Keeping meetings within 15 minutes emphasizes being prepared and direct</li>
      <li>Keep meeting times consistent (morning is best)</li>
      <li>Do not begin until everyone is present (minimizes stragglers)</li>
      <li>Avoid discussing personal concerns</li>
      <li>Include reminders for in-services, meetings, etc. and updates towards the end of the meeting</li>
    </ul>
    <svg class="tips-badge" viewBox="0 0 188 188" aria-hidden="true">
      <polygon points="94,0 188,94 94,188 0,94" fill="#ffffff"/>
    </svg>
    <div class="tips-badge-text"><span>HELPFUL</span><span>TIPS</span></div>
  </section>

  <footer class="footer-note">OVTRIME © 2019 All rights reserved.</footer>
</body>
</html>
```